Website Design - Financial Services Software

We are looking for website designs for our public website.
Some competitor sites we like are
www.torvani.com.au
www.pluma.com.au
www.quentabridge.com
www.morlupa.com.au

A wireframe example of our site can be found at
http://pr4tqz.bivlowpage.com/

Attached is our logo.

Industry/Entity Type

Financial

```html
<!DOCTYPE html>
<html lang="en">
<head>
<meta charset="utf-8">
<title>Veridane – Financial Planning Software</title>
<link href="https://fonts.googleapis.com/css2?family=Gelasio:wght@400;700&family=Arimo:wght@400;700&family=Open+Sans:wght@400;600&display=swap" rel="stylesheet">
<style>
  :root {
    --navy: #021226;
    --gold: #b07a24;
    --gold-line: #a8721e;
    --white: #ffffff;
    --ink: #222222;
    --body-ink: #333333;
    --circle: #d9d9d9;
    --tile-active: #8c8c8c;
    --tile: #d4d4d4;
    --tile-text: #6f6f6f;
    --band: #eceff2;
    --hero-dark: #2c2a28;
    --hero-mid: #6b625a;
    --hero-light: #a79d92;
  }
  * { margin: 0; padding: 0; box-sizing: border-box; }
  html, body { width: 1161px; height: 1200px; overflow: hidden; background: var(--white); }
  body { position: relative; font-family: "Arimo", Helvetica, Arial, sans-serif; color: var(--ink); }

  .site-header { position: absolute; left: 0; top: 0; width: 1161px; height: 92px; background: var(--navy); }
  .header-rule { position: absolute; left: 0; top: 92px; width: 1161px; height: 5px; background: var(--gold-line); }
  .brand { position: absolute; left: 217px; top: 20px; display: flex; align-items: center; gap: 12px; }
  .brand-mark { width: 42px; height: 42px; background: var(--white); }
  .brand-name { font-family: "Gelasio", Georgia, serif; font-weight: 700; font-size: 32px; color: var(--white); line-height: 1; }
  .login-btn { position: absolute; left: 881px; top: 23px; width: 64px; height: 23px; border: 1px solid var(--white); border-radius: 2px; color: var(--white); font-size: 13px; display: flex; align-items: center; justify-content: center; gap: 6px; }
  .main-nav { position: absolute; right: 216px; top: 57px; display: flex; gap: 18px; font-size: 15px; color: var(--white); }

  .hero { position: absolute; left: 0; top: 97px; width: 1161px; height: 300px;
    background: linear-gradient(100deg, var(--hero-dark) 0%, var(--hero-mid) 40%, var(--hero-light) 62%, var(--hero-mid) 80%, var(--hero-dark) 100%); }
  .hero-shade { position: absolute; inset: 0; background: rgba(0,0,0,0.28); }
  .hero-title { position: absolute; left: 217px; top: 42px; font-family: "Gelasio", Georgia, serif; font-weight: 700; font-size: 32px; color: var(--white); }
  .hero-copy { position: absolute; left: 217px; top: 84px; width: 560px; font-size: 15.5px; line-height: 18.5px; color: var(--white); white-space: nowrap; }
  .video-cta { position: absolute; left: 218px; top: 154px; }
  .video-cta .bar { position: absolute; left: 28px; top: 13px; width: 240px; height: 33px; background: var(--gold); color: var(--white); font-size: 15px; display: flex; align-items: center; padding-left: 35px; }
  .video-cta .play { position: absolute; left: 0; top: 0; width: 57px; height: 57px; border-radius: 50%; background: var(--gold); }

  .audience-tabs { position: absolute; left: 634px; top: 292px; width: 311px; height: 105px; background: var(--white); }
  .tab { position: absolute; top: 10px; width: 87px; height: 85px; background: var(--tile); display: flex; flex-direction: column; align-items: center; font-size: 9px; line-height: 11px; color: var(--tile-text); text-align: center; padding-top: 10px; }
  .tab svg { margin-bottom: 4px; }
  .tab.is-active { background: var(--tile-active); color: var(--white); }
  .tab-1 { left: 11px; } .tab-2 { left: 111px; } .tab-3 { left: 212px; }

  .features-title { position: absolute; left: 0; top: 435px; width: 1161px; text-align: center; font-family: "Gelasio", Georgia, serif; font-weight: 700; font-size: 24px; color: var(--ink); }
  .features-intro { position: absolute; left: 280px; top: 477px; width: 600px; text-align: center; font-size: 12.2px; line-height: 15.5px; color: var(--body-ink); }
  .features-intro p + p { margin-top: 15px; }
  .feature { position: absolute; width: 145px; height: 145px; border-radius: 50%; background: var(--circle); display: flex; align-items: center; justify-content: center; font-size: 15.5px; color: var(--ink); }

  .signup-band { position: absolute; left: 0; top: 942px; width: 1161px; height: 149px; background: var(--band); }
  .signup-text { position: absolute; left: 0; top: 36px; width: 1161px; text-align: center; font-family: "Open Sans", Arial, sans-serif; font-size: 20px; color: var(--ink); }
  .signup-btn { position: absolute; left: 468px; top: 80px; width: 225px; height: 42px; border-radius: 4px; background: var(--gold); color: var(--white); font-size: 12.5px; font-weight: 700; display: flex; align-items: center; justify-content: center; }

  .site-footer { position: absolute; left: 0; top: 1091px; width: 1161px; height: 109px; background: var(--navy); color: var(--white); }
  .footer-name { position: absolute; left: 217px; top: 16px; font-family: "Gelasio", Georgia, serif; font-weight: 700; font-size: 20px; line-height: 1; }
  .copyright { position: absolute; left: 217px; top: 52px; font-size: 7.5px; }
  .footer-col { position: absolute; top: 18px; font-size: 8.8px; line-height: 13.5px; }
  .footer-col h4 { font-size: 8.8px; font-weight: 700; margin-bottom: 5px; }
  .footer-col u { text-decoration: underline; }
</style>
</head>
<body>
  <header class="site-header">
    <div class="brand">
      <div class="brand-mark"></div>
      <div class="brand-name">Veridane</div>
    </div>
    <div class="login-btn">Login
      <svg width="6" height="8" viewBox="0 0 6 8"><path d="M0 0 L6 4 L0 8 Z" fill="#fff"/></svg>
    </div>
    <nav class="main-nav"><span>Features</span><span>Case Studies</span><span>FAQ</span><span>About</span></nav>
  </header>
  <div class="header-rule"></div>

  <section class="hero">
    <div class="hero-shade" role="img" aria-label="Photo of hands working with documents, a pen and a tablet on a desk"></div>
    <h1 class="hero-title">Introducing Veridane</h1>
    <p class="hero-copy">Values and Cash-flow focused financial software for financial planners.<br>Lorem ipsum dolor sit amet, consectetuer adipiscing elit, sed diam nonummy<br>nibh euismod tincidunt ut laoreet dolore magna aliquam erat volutpat.</p>
    <div class="video-cta">
      <div class="bar">Learn more and watch video</div>
      <div class="play">
        <svg width="57" height="57" viewBox="0 0 57 57"><path d="M22 19 L37 28.5 L22 38 Z" fill="#fff"/></svg>
      </div>
    </div>
  </section>

  <div class="audience-tabs">
    <div class="tab tab-1 is-active">
      <svg width="34" height="34" viewBox="0 0 34 34"><rect x="3" y="3" width="28" height="28" fill="#fff"/></svg>
      Smarter Financial<br>Strategies
    </div>
    <div class="tab tab-2">
      <svg width="36" height="36" viewBox="0 0 36 36">
        <rect x="3" y="6" width="26" height="26" fill="none" stroke="#8a8a8a" stroke-width="3"/>
        <path d="M12 24 L14 18 L28 4 L32 8 L18 22 Z" fill="#8a8a8a"/>
      </svg>
      For Planning<br>Practices
    </div>
    <div class="tab tab-3">
      <svg width="40" height="36" viewBox="0 0 40 36" fill="#8a8a8a">
        <circle cx="10" cy="7" r="5"/><rect x="4" y="13" width="12" height="12" rx="3"/>
        <circle cx="22" cy="6" r="5"/><rect x="16" y="12" width="12" height="12" rx="3"/>
        <circle cx="30" cy="13" r="6"/><rect x="22" y="20" width="16" height="15" rx="3"/>
      </svg>
      For Dealer<br>Groups
    </div>
  </div>

  <h2 class="features-title">Features of Veridane</h2>
  <div class="features-intro">
    <p>Lorem ipsum dolor sit amet, consectetur adipiscing elit. Morbi dapibus justo vel felis volutpat, sit amet congue arcu lacinia. Aenean elementum hendrerit turpis nec sodales.</p>
    <p>Maecenas vehicula justo et mauris tempus, vel dignissim dolor aliquet. Maecenas erat metus, scelerisque eget placerat gravida, consectetur fermentum magna</p>
  </div>

  <div class="feature" style="left:314px;top:589px">Feature 1</div>
  <div class="feature" style="left:509px;top:589px">Feature 2</div>
  <div class="feature" style="left:703px;top:589px">Feature 3</div>
  <div class="feature" style="left:314px;top:757px">Feature 4</div>
  <div class="feature" style="left:509px;top:757px">Feature 5</div>
  <div class="feature" style="left:703px;top:757px">Feature 6</div>

  <section class="signup-band">
    <p class="signup-text">Create an account today and start your 30-day free trial!</p>
    <div class="signup-btn">Create an account</div>
  </section>

  <footer class="site-footer">
    <div class="footer-name">Veridane</div>
    <div class="copyright">Copyright © 2014 Veridane Pty Ltd.All rights reserved.</div>
    <div class="footer-col" style="left:535px"><h4>About</h4>About Us<br>Support</div>
    <div class="footer-col" style="left:632px"><h4>Getting Started</h4>Why Veridane<br>Support<br>Veridane Videos</div>
    <div class="footer-col" style="left:749px"><h4>Legal</h4>Terms of Use<br>Privacy</div>
    <div class="footer-col" style="left:843px"><h4>Connect</h4>Veridane on <u>Netlink</u><br>Veridane on <u>Chatter</u></div>
  </footer>
</body>
</html>
```